Brochure Design Project

Our company is TEM Bexley Fold. (no LOGO)

We are a restaurant marketing and advertising service. We market restaurants menus by producing a menu guide, distributing flyers and post cards, and also placing the restaurants menu on our website for delivery.

We make restaurants more profitable, by making their food more accessible. Marketing restaurants on search engines, websites, friendloop, vrop, zindle, and a total of 21 different marketing techniques that make restaurants more money.

Key Point: This is all done at NO COST to the restaurant.

We are looking for a design for a brochure that will be mailed as well as handed to restaurateurs.

In my attached file I am including our sales letter. The letter can stay in letter form for the inside of a tri-fold brochure or it can be part of your design.

For more information about our service, please read the attached sales letter.

Target Market(s)

Restaurant Owners and General managers

Industry/Entity Type

Advertising

Requirements
Must have
• Must look attractive and Eye-catching

```html
<!DOCTYPE html>
<html lang="en">
<head>
<meta charset="utf-8">
<title>TEM Bexley Fold – Brochure</title>
<link href="https://fonts.googleapis.com/css2?family=Tinos:wght@400;700&family=Tenor+Sans&family=Arimo&display=swap" rel="stylesheet">
<style>
  :root {
    --page: #ffffff;
    --panel: #072025;
    --heading: #414c4e;
    --body: #525d5f;
    --strong: #4a4a4a;
    --white: #ffffff;
    --arrow: #1f6ec2;
  }
  * { margin: 0; padding: 0; box-sizing: border-box; }
  html, body { width: 1200px; height: 1000px; overflow: hidden; background: var(--page); }
  .canvas { position: relative; width: 1200px; height: 1000px; }

  .panel { position: absolute; background: var(--panel); overflow: hidden; }
  .panel--cover { left: 0; top: 0; width: 459px; height: 661px; }
  .panel--pitch { left: 743px; top: 0; width: 457px; height: 660px; }
  .panel--letter { left: 266px; top: 660px; width: 703px; height: 340px; }

  .tagline {
    position: absolute; font-family: "Arimo", Arial, sans-serif;
    font-size: 14.5px; color: var(--white); white-space: nowrap;
  }
  .panel--cover .tagline { left: 0; width: 100%; text-align: center; top: 588px; }
  .panel--pitch .tagline { left: 0; width: 100%; text-align: center; top: 586px; }

  .cover__name {
    position: absolute; left: 0; top: 276px; width: 100%; text-align: center;
    font-family: "Tinos", "Times New Roman", serif; font-size: 40px;
    color: var(--white); letter-spacing: 1px;
  }

  .pitch__arrow { position: absolute; left: 9px; width: 36px; height: 22px; }
  .pitch__heading {
    position: absolute; left: 56px; font-family: "Tenor Sans", sans-serif;
    font-weight: 400; font-size: 15px; letter-spacing: 5px; line-height: 20.5px;
    color: var(--heading); text-transform: uppercase;
  }
  .pitch__heading--check { top: 75px; }
  .pitch__heading--tired { top: 186px; }
  .pitch__body {
    position: absolute; left: 56px; top: 260px; width: 360px;
    font-family: "Tinos", "Times New Roman", serif; font-size: 11px;
    line-height: 15.2px; color: var(--body); letter-spacing: -0.1px;
  }
  .pitch__body p { margin-bottom: 7px; }
  .pitch__guarantee {
    position: absolute; left: 55px; top: 515px;
    font-family: "Tinos", "Times New Roman", serif; font-weight: 700;
    font-size: 27px; color: var(--strong);
  }

  .letter {
    position: absolute; left: 190px; top: -90px; width: 260px; height: 520px;
    transform: rotate(90deg); transform-origin: center;
    font-family: "Tinos", "Times New Roman", serif; font-size: 10px;
    line-height: 16px; color: var(--body);
  }
  .letter p { width: 260px; }
  .letter__lead { margin-bottom: 31px; }
  .letter__question { font-size: 12.5px; margin-bottom: 23px; }
  .letter__call { margin-bottom: 38px; }
  .letter__call strong, .letter__contact { font-weight: 700; text-decoration: underline; font-size: 12.5px; }
  .letter__signoff { text-decoration: underline; font-size: 11.5px; margin-bottom: 22px; }
  .letter__signer { font-size: 10.5px; margin-bottom: 18px; }
  .letter__contact { display: block; line-height: 16px; margin-bottom: 18px; }
  .letter__contact--site { margin-bottom: 36px; }
  .letter__ps { font-size: 12.5px; text-decoration: underline; margin-bottom: 6px; }
  .letter__ps-note { font-size: 9.5px; line-height: 14px; }
  .letter .tagline { position: absolute; left: 60px; bottom: 0; font-size: 14.5px; line-height: 17px; }
</style>
</head>
<body>
<div class="canvas">

  <section class="panel panel--cover">
    <h1 class="cover__name">TEM Bexley Fold</h1>
    <p class="tagline">Advertisement was Never Simpler</p>
  </section>

  <section class="panel panel--pitch">
    <svg class="pitch__arrow" style="top:73px" viewBox="0 0 36 22"><path d="M0 7h22V0l14 11-14 11v-7H0z" fill="var(--arrow)"/></svg>
    <svg class="pitch__arrow" style="top:146px" viewBox="0 0 36 22"><path d="M0 7h22V0l14 11-14 11v-7H0z" fill="var(--arrow)"/></svg>
    <svg class="pitch__arrow" style="top:522px" viewBox="0 0 36 22"><path d="M0 7h22V0l14 11-14 11v-7H0z" fill="var(--arrow)"/></svg>

    <h2 class="pitch__heading pitch__heading--check">Would a check for<br>$18,375 with your<br>restaurants name on it<br>be worth a 15 min<br>conversation?</h2>
    <h2 class="pitch__heading pitch__heading--tired">Are you tired of<br>ineffective marketing<br>and advertising?</h2>

    <div class="pitch__body">
      <p>If you answered yes to either question, we should talk about our all-inclusive marketing plan. Our marketing plan places your menu in front of thousands of customers each and every month. Hungry customers looking to buy immediately. Hungry customers that want food now. The more views your menu receives, the more likely a customer will purchase food from your restaurant.</p>
      <p>Ever have a problem with down time at your restaurant? Customers are not dining in or taking out because it’s too hot or too cold or it’s raining outside? That's a problem that you wouldn’t have to have, if you made your food more accessible.</p>
      <p>TEM Bexley Fold is a full service restaurant marketing and advertising service that specializes in delivery. We deliver food from a variety of restaurants to people at their homes, offices, and hotels! Using our marketing plan we will bring more exposure to your restaurant and increase your bottom line.</p>
    </div>

    <p class="pitch__guarantee">WE GUARANTEE IT!</p>
    <p class="tagline">Advertisement was Never Simpler</p>
  </section>

  <section class="panel panel--letter">
    <div class="letter">
      <p class="letter__lead">We guarantee that you will only make money and not pay money. There are never any participation costs, or fees associated with our service. We use a combination of 21 proven Marketing techniques to drive your profits up while keeping cost down.</p>
      <p class="letter__question">So what should you do?</p>
      <p class="letter__call">Call me now at <strong>555-214-3870</strong> to schedule a 15 min consultation that is guaranteed to NOT cost you anything and only make your restaurant money.</p>
      <p class="letter__signoff">Talk to you soon!</p>
      <p class="letter__signer">Ray Holloway</p>
      <span class="letter__contact">555-214-3870</span>
      <span class="letter__contact letter__contact--site">Tembexleyfold.com</span>
      <p class="letter__ps">P.S</p>
      <p class="letter__ps-note">I have a check with your restaurants name on it, so contact me before July 26, 2019! You can also schedule an appointment online at tembexleyfold.com</p>
      <p class="tagline">Advertisement was Never Simpler</p>
    </div>
  </section>

</div>
</body>
</html>
```